Luxury Brand Real Estate For Sale sign

**Update** I've added some examples from the internet of other signs that have a look similar to what I would like to see. I do not want my personal name in the sign. And the word FOR SALE Does not need to be so large - it can be more subtle.
I want to create a Real Estate for sale sign for my company that will be used for luxury/higher end real estate listings. I’m sharing my business card as well as a logo with new teal color to show what we're moving towards: we’re using Teal, white, black and gold.
Hoping the sign is simple, sophisticated and eye catching.
The sign should be 24" wide by 30" tall including the company name: Harbor Crest Realty Group and our logo, office phone number 727-555-0148 and website www.hcrgexample.com the words "For Sale"
Optional to add this e-mail address info@hcrgexample.com to the sign
Target Market(s)
Luxury home buyers
Industry/Entity Type
Real Estate
Look and feel

```html
<!DOCTYPE html>
<html lang="en">
<head>
<meta charset="utf-8">
<title>Harbor Crest Realty Group – For Sale Signs</title>
<link rel="stylesheet" href="https://fonts.googleapis.com/css2?family=Montserrat:wght@400;600;700;800&display=swap">
<style>
  :root {
    --backdrop: #ededed;
    --sign-black: #0b0b0b;
    --frame-white: #ffffff;
    --brand-cyan: #2ec4f1;
    --text-white: #ffffff;
  }
  html, body {
    margin: 0;
    width: 1200px;
    height: 590px;
    overflow: hidden;
    background: var(--backdrop);
    font-family: "Montserrat", sans-serif;
  }
  .sign {
    position: absolute;
    top: 104px;
    width: 305px;
    height: 382px;
  }
  .sign--cyan { left: 142px; }
  .sign--white { left: 752px; }
  .sign__panel { fill: var(--sign-black); }
  .sign__frame { fill: none; stroke: var(--frame-white); stroke-width: 1.6; }
  .sign__headline { font-family: "Montserrat", sans-serif; font-weight: 800; font-size: 84px; }
  .sign--cyan .sign__headline { fill: var(--brand-cyan); }
  .sign--white .sign__headline { fill: var(--text-white); }
  .sign__rule { stroke-width: 2; }
  .sign--cyan .sign__rule { stroke: var(--brand-cyan); }
  .sign--white .sign__rule { stroke: var(--text-white); }
  .sign__phone { fill: var(--text-white); font-family: "Montserrat", sans-serif; font-weight: 700; font-size: 33px; }
  .sign__web { fill: var(--text-white); font-family: "Montserrat", sans-serif; font-weight: 400; font-size: 18px; }
  .brand__mark { fill: none; stroke: var(--brand-cyan); stroke-width: 1.4; }
  .brand__name { fill: var(--brand-cyan); font-family: "Montserrat", sans-serif; font-weight: 600; font-size: 10.5px; }
</style>
</head>
<body>

<svg class="sign sign--cyan" viewBox="0 0 305 382" role="group" aria-label="For Sale sign, cyan headline">
  <rect class="sign__panel" width="305" height="382"/>
  <path class="sign__frame" d="M28 16 H277 A13 13 0 0 0 290 29 V351 A13 13 0 0 0 277 364 H28 A13 13 0 0 0 15 351 V29 A13 13 0 0 0 28 16 Z"/>
  <text class="sign__headline" x="70" y="114" textLength="170" lengthAdjust="spacingAndGlyphs">FOR</text>
  <text class="sign__headline" x="49" y="183" textLength="207" lengthAdjust="spacingAndGlyphs">SALE</text>
  <line class="sign__rule" x1="75" y1="190" x2="231" y2="190"/>
  <text class="sign__phone" x="49" y="250" textLength="207" lengthAdjust="spacingAndGlyphs">727-555-0148</text>
  <text class="sign__web" x="49" y="274" textLength="207" lengthAdjust="spacingAndGlyphs">www.hcrgexample.com</text>
  <g class="brand">
    <rect class="brand__mark" x="75" y="319" width="22" height="22"/>
    <text class="brand__name" x="105" y="328">HARBOR CREST</text>
    <text class="brand__name" x="105" y="341">REALTY GROUP</text>
  </g>
</svg>

<svg class="sign sign--white" viewBox="0 0 305 382" role="group" aria-label="For Sale sign, white headline">
  <rect class="sign__panel" width="305" height="382"/>
  <path class="sign__frame" d="M28 16 H277 A13 13 0 0 0 290 29 V351 A13 13 0 0 0 277 364 H28 A13 13 0 0 0 15 351 V29 A13 13 0 0 0 28 16 Z"/>
  <text class="sign__headline" x="70" y="114" textLength="170" lengthAdjust="spacingAndGlyphs">FOR</text>
  <text class="sign__headline" x="49" y="183" textLength="207" lengthAdjust="spacingAndGlyphs">SALE</text>
  <line class="sign__rule" x1="75" y1="190" x2="231" y2="190"/>
  <text class="sign__phone" x="49" y="250" textLength="207" lengthAdjust="spacingAndGlyphs">727-555-0148</text>
  <text class="sign__web" x="49" y="274" textLength="207" lengthAdjust="spacingAndGlyphs">www.hcrgexample.com</text>
  <g class="brand">
    <rect class="brand__mark" x="75" y="319" width="22" height="22"/>
    <text class="brand__name" x="105" y="328">HARBOR CREST</text>
    <text class="brand__name" x="105" y="341">REALTY GROUP</text>
  </g>
</svg>

</body>
</html>
```